Marrow medical spa and wellness

Integrate existing logo and web design (colors and background) into tri fold, single card brochure and business card design. We already have a logo and an idea for our promotional material but we would like someone to bring it together for us! Quenvoraspaandwellness.com. We want to see what a marble background with a faded lily (as seen on our webpage) would look like on brochures and business cards.

```html
<!DOCTYPE html>
<html lang="en">
<head>
<meta charset="utf-8">
<title>Marrow Medical Spa &amp; Wellness – Business Card</title>
<link href="https://fonts.googleapis.com/css2?family=Jost:wght@400&family=Dancing+Script:wght@600&display=swap" rel="stylesheet">
<style>
  :root {
    --backdrop: #2a2a2b;
    --card: #161616;
    --gold: #d9ad2b;
    --ink-light: #e8e8e8;
    --rule: #8a8a8a;
  }
  html, body {
    margin: 0;
    width: 1200px;
    height: 1017px;
    overflow: hidden;
    background: var(--backdrop);
    font-family: "Jost", "Futura", sans-serif;
  }
  .sheet {
    position: relative;
    width: 1200px;
    height: 1017px;
  }
  .card {
    position: absolute;
    left: 200px;
    width: 800px;
    height: 457px;
    background: var(--card);
    box-shadow: 0 18px 40px rgba(0,0,0,.45);
    box-sizing: border-box;
    padding: 40px;
  }
  .card--front { top: 34px; }
  .card--back { top: 526px; }

  .brand {
    position: absolute;
    inset: 0;
    display: flex;
    align-items: center;
    justify-content: center;
  }
  .brand__name {
    color: var(--gold);
    font-size: 34px;
    font-weight: 400;
    letter-spacing: 3px;
    text-transform: uppercase;
    white-space: nowrap;
  }

  .back-layout {
    position: absolute;
    inset: 0;
    display: flex;
    align-items: center;
    justify-content: center;
  }
  .back-block {
    display: flex;
    flex-direction: column;
    align-items: flex-start;
  }
  .holder {
    margin: 0 0 18px;
    color: var(--gold);
    font-family: "Dancing Script", cursive;
    font-weight: 600;
    font-size: 54px;
    line-height: 1;
    white-space: nowrap;
  }
  .details {
    display: flex;
    align-items: stretch;
    color: var(--ink-light);
    font-size: 18px;
    line-height: 1.4;
    white-space: nowrap;
  }
  .address {
    font-style: normal;
    padding-right: 22px;
  }
  .divider {
    width: 1px;
    background: var(--rule);
  }
  .contact {
    list-style: none;
    margin: 0;
    padding: 0 0 0 22px;
  }
  .contact li {
    display: flex;
    align-items: center;
    gap: 10px;
  }
  .contact svg {
    width: 15px;
    height: 15px;
    flex: none;
    fill: var(--gold);
  }
</style>
</head>
<body>
<main class="sheet">
  <section class="card card--front" aria-label="Card front">
    <div class="brand">
      <span class="brand__name">Marrow Medical Spa &amp; Wellness</span>
    </div>
  </section>

  <section class="card card--back" aria-label="Card back">
    <div class="back-layout">
      <div class="back-block">
        <h1 class="holder">Daniel Hartwell</h1>
        <div class="details">
          <address class="address">
            4821 W. Cedar<br>Road, Suite 12<br>Glendale, AZ 85310
          </address>
          <span class="divider"></span>
          <ul class="contact">
            <li>
              <svg viewBox="0 0 24 24" aria-hidden="true"><path d="M6.6 10.8a15.1 15.1 0 0 0 6.6 6.6l2.2-2.2c.3-.3.7-.4 1-.2 1.1.4 2.3.6 3.6.6.6 0 1 .4 1 1V20c0 .6-.4 1-1 1A17 17 0 0 1 3 4c0-.6.4-1 1-1h3.5c.6 0 1 .4 1 1 0 1.3.2 2.5.6 3.6.1.3 0 .7-.2 1z"/></svg>
              (602) 555-0148
            </li>
            <li>
              <svg viewBox="0 0 24 24" aria-hidden="true"><path d="M2 5h20v14H2z M3.5 6.5 12 13l8.5-6.5" stroke="#161616" stroke-width="1.4"/></svg>
              welcome@quenvoraspaandwellness.com
            </li>
            <li>
              <svg viewBox="0 0 24 24" aria-hidden="true"><circle cx="12" cy="12" r="10"/><path d="M2 12h20M12 2c3 3 3 17 0 20M12 2c-3 3-3 17 0 20" stroke="#161616" stroke-width="1.4" fill="none"/></svg>
              www.quenvoraspaandwellness.com
            </li>
          </ul>
        </div>
      </div>
    </div>
  </section>
</main>
</body>
</html>
```